Ketwinall Need to look more professional with our Word Press design

I need to change the look of our Word Press site. Must haves- Newsletter option, contact page refer to www.ketwinall.com.au

Industry/Entity Type

It Professional

```html
<!DOCTYPE html>
<html lang="en">
<head>
<meta charset="utf-8">
<title>Ketwinall – Key Account Management Services</title>
<link rel="stylesheet" href="https://fonts.googleapis.com/css2?family=Lato:wght@400;700&family=Open+Sans:wght@300;400;600;700&family=Tinos:ital@1&display=swap">
<style>
:root{
  --ink:#1e1d24;
  --orange:#f26a0f;
  --orange-light:#f7941d;
  --yellow:#fdc513;
  --header-bg:#e7e7ea;
  --text:#3a3a3a;
  --rule:#cfcfcf;
  --social:#1d72c4;
  --quote-bg:#efefef;
  --white:#ffffff;
}
*{margin:0;padding:0;box-sizing:border-box}
html,body{width:816px;height:1200px;overflow:hidden;background:var(--white)}
body{position:relative;font-family:"Open Sans",Arial,sans-serif;color:var(--text)}
.abs{position:absolute}

/* top bar */
.topbar{left:0;top:0;width:816px;height:22px;background:var(--ink)}
.social{display:flex;gap:4px}
.social span{width:13px;height:13px;border-radius:50%;background:var(--social);display:block}
.search-field{left:527px;top:4px;width:89px;height:15px;background:#33323a;color:#8a8a90;font-size:6px;padding:4px 0 0 3px}
.search-btn{left:625px;top:3px;width:24px;height:17px;background:var(--orange)}

/* header */
.header{left:0;top:22px;width:816px;height:73px;background:var(--header-bg)}
.stripe{height:7px;background:var(--yellow);top:55px}
.brand{left:176px;top:51px;font-size:11.5px;font-weight:700;color:var(--ink);letter-spacing:-.3px;line-height:14px}
.brand-tag{left:240px;top:55px;font-size:4.6px;font-weight:600;color:var(--ink);line-height:7px;white-space:nowrap}
.nav{top:54px;font-size:8.5px;color:var(--ink)}
.nav a{color:inherit;text-decoration:none;position:absolute;white-space:nowrap}
.nav a.active{color:var(--orange)}

/* hero */
.hero-photo{left:0;top:95px;width:816px;height:179px;background:linear-gradient(90deg,#34373d 0%,#4a4f57 25%,#8b7b72 50%,#5a5d63 75%,#3a3d43 100%)}
.hero-title{left:0;width:816px;top:106px;text-align:center;color:var(--white);font-weight:300;font-size:78px;line-height:90px;letter-spacing:-1px}
.hero-sub{left:0;width:816px;top:175px;text-align:center;color:var(--white);font-weight:300;font-size:25px}
.arrow{width:0;height:0;border-top:21px solid transparent;border-bottom:21px solid transparent}
.arrow.left{border-right:20px solid var(--yellow)}
.arrow.right{border-left:20px solid var(--yellow)}
.btn{display:flex;align-items:center;justify-content:center;color:var(--white);font-weight:700;font-size:8px;letter-spacing:.2px}
.btn.orange{background:var(--orange)}
.btn.dark{background:var(--ink)}

/* feature band */
.poly-band{left:0;top:274px;width:816px;height:96px;background:linear-gradient(90deg,#f4a52a 0%,#fdc43a 25%,#f39a2c 45%,#3aa58f 70%,#0e6e7a 100%)}
.card{width:155px;height:106px;top:284px;background:var(--ink);box-shadow:0 8px 6px -4px rgba(0,0,0,.45);text-align:center;overflow:hidden}
.card-pic{width:50px;height:50px;border-radius:50%;margin:12px auto 0;border:2px solid var(--white)}
.card h3{font-family:"Lato",sans-serif;font-size:8.5px;line-height:10px;color:var(--orange);margin-top:3px}
.card p{font-size:5.6px;color:var(--white);line-height:10px;margin:3px 3px 0;letter-spacing:-.05px}

/* partners */
.partner{top:444px;height:36px;border-radius:4px}

/* section headings */
.section-title{font-family:"Lato",sans-serif;font-weight:700;color:var(--orange);font-size:14.5px}
.rule{height:2px;background:var(--rule)}
.body-copy{font-size:6.6px;line-height:12.2px;color:var(--text)}

/* quote */
.quote{left:494px;top:820px;width:155px;height:145px;background:var(--quote-bg)}
.quote-mark{position:absolute;left:0;width:155px;text-align:center;font-family:"Tinos",serif;font-size:34px;color:var(--orange);font-weight:700;line-height:30px}
.quote p{position:absolute;left:12px;top:38px;width:131px;text-align:center;font-family:"Tinos",serif;font-style:italic;font-size:6.6px;line-height:12.4px;color:var(--text)}

/* footer */
.footer-bg{left:0;top:993px;width:816px;height:207px;background:linear-gradient(135deg,#f26a0f 0%,#f7891c 40%,#fba227 70%,#f9b233 100%)}
.footer-text{color:var(--white);font-size:6.6px}
.field{background:var(--white)}
.label{color:var(--white);font-size:5.4px}
.contact-block{right:199px;text-align:right;color:var(--white)}
.footer-nav{top:1175px;left:0;width:816px;text-align:center;font-size:7px;color:var(--ink)}
.footer-nav a{color:inherit;text-decoration:none;margin:0 5px}
</style>
</head>
<body>

<!-- top bar -->
<div class="abs topbar"></div>
<div class="abs social" style="left:168px;top:5px"><span></span><span></span><span></span></div>
<div class="abs search-field">Search</div>
<div class="abs search-btn">
  <svg width="24" height="17" viewBox="0 0 24 17"><circle cx="11" cy="7.5" r="4" fill="none" stroke="#fff" stroke-width="2"/><line x1="14" y1="10.5" x2="17" y2="13.5" stroke="#fff" stroke-width="2.4" stroke-linecap="round"/></svg>
</div>

<!-- header -->
<div class="abs header"></div>
<div class="abs stripe" style="left:0;width:342px"></div>
<div class="abs stripe" style="left:654px;width:162px"></div>
<div class="abs brand">Ketwinall</div>
<div class="abs brand-tag">KEY ACCOUNT MANAGEMENT SERVICES</div>
<nav class="abs nav" style="left:0">
  <a class="active" style="left:358px">HOME</a>
  <a style="left:400px">ABOUT US</a>
  <a style="left:457px">AUSTRALIAN FOOD BROKERS</a>
  <a style="left:588px">CONTACT US</a>
</nav>

<!-- hero -->
<div class="abs hero-photo" role="img" aria-label="Blurred restaurant table setting with chairs and glassware"></div>
<div class="abs hero-title">EXPERTS</div>
<div class="abs hero-sub">in key account management</div>
<div class="abs arrow left" style="left:143px;top:165px"></div>
<div class="abs arrow right" style="left:653px;top:165px"></div>
<div class="abs btn orange" style="left:298px;top:235px;width:139px;height:19px">ABOUT US</div>
<div class="abs btn dark" style="left:446px;top:235px;width:136px;height:19px">AUSTRALIAN FOOD BROKERS</div>

<!-- feature band -->
<div class="abs poly-band" role="img" aria-label="Low-poly geometric band in yellow, orange and teal"></div>
<div class="abs card" style="left:167px">
  <div class="card-pic" style="background:#e53b2c"></div>
  <h3>Hospitality Trade Network</h3>
  <p>Curabitur ultricies, nunc id adipiscing feugiat, leo nunc posuere mi, at facilisis lacus metus eu tellus.</p>
</div>
<div class="abs card" style="left:331px">
  <div class="card-pic" role="img" aria-label="Portrait photo of the director" style="background:#8d7a6c"></div>
  <h3>Why us</h3>
  <p>Curabitur ultricies, nunc id adipiscing feugiat, leo nunc posuere mi, at facilisis lacus metus eu tellus.</p>
</div>
<div class="abs card" style="left:494px">
  <div class="card-pic" role="img" aria-label="Photo of a restaurant interior" style="background:#b89878"></div>
  <h3>Our logistics</h3>
  <p>Curabitur ultricies, nunc id adipiscing feugiat, leo nunc posuere mi, at facilisis lacus metus eu tellus.</p>
</div>

<!-- partners -->
<div class="abs arrow left" style="left:167px;top:441px"></div>
<div class="abs arrow right" style="left:629px;top:441px"></div>
<div class="abs partner" style="left:222px;width:42px;background:#c9cdd6"></div>
<div class="abs partner" style="left:287px;top:451px;width:48px;height:20px;border-radius:50%;background:#4a4d63"></div>
<div class="abs partner" style="left:361px;top:450px;width:53px;height:24px;border-radius:50%;background:#1e5fb4"></div>
<div class="abs partner" style="left:438px;top:446px;width:32px;height:34px;border-radius:0;background:#1f6b2c"></div>
<div class="abs partner" style="left:503px;top:447px;width:28px;height:32px;background:#d8352a"></div>
<div class="abs partner" style="left:556px;top:445px;width:36px;height:36px;background:#dddddd"></div>

<!-- experts -->
<div class="abs section-title" style="left:0;width:816px;text-align:center;top:512px">Foodservice Experts</div>
<div class="abs rule" style="left:167px;top:534px;width:482px"></div>
<div class="abs" role="img" aria-label="Portrait photo of the director" style="left:168px;top:552px;width:91px;height:91px;border-radius:50%;border:2px solid var(--orange-light);background:#a58a78"></div>
<p class="abs body-copy" style="left:265px;top:559px;width:386px">Hi, my name is <b><i>Daniel Hartwell</i></b>. It is my privilege to bring to you a successful combination of over 20 years experience in Foodservice, sales and marketing to your business. Through my latest successful venture, Ketwinall, working with you, my aim is to provide you with more... More ....... Sales by performance More ....... Insight on the End-User More ....... Alignment with the Customer More ....... Integrated solutions to create real customer value</p>
<div class="abs btn orange" style="left:510px;top:614px;width:139px;height:19px">READ MORE</div>

<div class="abs" role="img" aria-label="Rows of plated dishes on a banquet table, softly blurred" style="left:167px;top:660px;width:482px;height:146px;background:linear-gradient(180deg,#3d3a36 0%,#9a8f85 35%,#d9d2c8 65%,#f4f2ef 100%)"></div>

<!-- network -->
<div class="abs section-title" style="left:166px;top:819px">Hospitality Trade Network</div>
<div class="abs rule" style="left:167px;top:841px;width:318px"></div>
<p class="abs body-copy" style="left:167px;top:851px;width:322px"><b>HOSPITALITY TRADE NETWORK</b> is the NATIONAL organisation representing the broadest range of businesses involved with the Foodservice Industry throughout Australia. The HTN works collaboratively with the food &amp; beverage industry and other similar organisations in each state, to work together and to assist each other with business, networking and to enrich the foodservice industry as a whole. HTN is a portal of information and hosts events to engage with industry, to learn from the leaders in the industry and to provide numerous opportunities to network with the broadest range of member companies and their teams. Business events are held throughout Australia.</p>
<div class="abs btn orange" style="left:346px;top:943px;width:139px;height:20px">READ MORE</div>

<div class="abs quote">
  <div class="quote-mark" style="top:6px">&ldquo;</div>
  <p>Ketwinall is now successfully established in Western Australia. We are thrilled to represent the following, dynamic companies within the Foodservice, Bakery Route and Food Manufactures channels</p>
  <div class="quote-mark" style="top:124px">&rdquo;</div>
</div>

<!-- footer -->
<div class="abs footer-bg" role="img" aria-label="Low-poly geometric pattern in orange tones"></div>
<div class="abs footer-text" style="left:167px;top:1018px">Contact us to take the first step now.</div>
<div class="abs label" style="left:167px;top:1039px">Name</div>
<div class="abs label" style="left:274px;top:1039px">Email</div>
<div class="abs label" style="left:381px;top:1039px">Organization</div>
<div class="abs field" style="left:167px;top:1048px;width:98px;height:15px"></div>
<div class="abs field" style="left:274px;top:1048px;width:98px;height:15px"></div>
<div class="abs field" style="left:381px;top:1048px;width:99px;height:15px"></div>
<div class="abs label" style="left:167px;top:1070px">Message</div>
<div class="abs field" style="left:167px;top:1079px;width:313px;height:41px"></div>
<div class="abs btn orange" style="left:338px;top:1128px;width:140px;height:20px">SUBMIT</div>

<div class="abs contact-block" style="top:1048px;font-size:6.6px;line-height:8px">PO Box 418<br>Northbrook WA 6920</div>
<div class="abs contact-block" style="top:1065px;font-size:15px">08 9100 4521</div>
<div class="abs contact-block" style="top:1091px;font-size:6.6px">sales@ketwinall.com.au</div>
<div class="abs social" style="left:569px;top:1109px"><span></span><span></span><span></span></div>

<div class="abs" style="left:167px;top:1161px;width:482px;height:1px;background:rgba(255,255,255,.6)"></div>
<nav class="abs footer-nav">
  <a>HOME</a><a>ABOUT US</a><a>AUSTRALIAN FOOD BROKERS</a><a>CONTACT US</a>
</nav>
<div class="abs" style="left:0;width:816px;top:1190px;text-align:center;font-size:5px;color:var(--ink)">© 2014 Ketwinall</div>

</body>
</html>
```